Vocational Mentor needs an impressive business card

1. I need a business card (or maybe three with identic look) to promote me and my three business titles/services:
- Vocational Mentor. I help people find their vocation and live happily from it. I use my 20 years of experience in business, management and psychology to help them identify the most efficient ways to make a living doing what they are passionate about.
- Business Angel. I help founders start a succesful business with minimum risks and costs. I use my 20 years of experience in sales, management and entrepreneurship to help them identify the most efficient ways, in terms of time and cost, to validate their business idea.
- Learning Designer. I design unique learning programs that produce long-term cognitive and behavioural changes to people and organisations. I use my 20 years of experience in learning, teaching and change management to create minimalist experiences and processes that allow them to change efficiently in their pursued direction.

2. I would like a two-sided business card, on the front with my name, contact details and titles, on the back the explanation of the services.
Updates

Hi all,

I updated my brief, included contacts info and give feedback on all designs I got. I am new on this platform so please tell me if you need anything else or if I don't use corectly the platform forms.

Kind regards,
Tudor

Hi all,

I shortened the services description by deleting the phrase "I call..."

Kind regards,
Tudor

Target Market(s)

Freelancers, startups, people and organization willing to invest in change through ultimate learning experiences

Industry/Entity Type

Business

Font styles to use
Serif

Requirements
Must have
• Front side: full name, titles, web site, email, phone like below:
Tudor Vasilache
Vocational Mentor, Business Angel, Learning Designer
info@tudorvasilache.example
www.tudorvasilache.example
+40-745-TUDORV
Nice to have
• Back side: the description of the services I provide as in the task description.
1/3: it would be nice if I can jam all three titles on the front side but then I need a solution to jam all three services on the back side.

```html
<!DOCTYPE html>
<html lang="en">
<head>
<meta charset="utf-8">
<title>Tudor Vasilache – Business Cards</title>
<link rel="stylesheet" href="https://fonts.googleapis.com/css2?family=Rosarivo&display=swap">
<style>
  :root {
    --orange: #e8732a;
    --brown: #7a4a22;
    --cream: #f3ead8;
    --cream-deep: #dcc49c;
    --ink-light: #fbf4e6;
    --page: #ffffff;
  }
  * { margin: 0; padding: 0; box-sizing: border-box; }
  html, body {
    width: 693px; height: 1200px; overflow: hidden;
    background: var(--page);
  }
  .sheet { position: relative; width: 693px; height: 1200px; }
  .card {
    position: absolute; left: 40px;
    width: 653px; height: 372px;
    font-family: "Rosarivo", Georgia, serif;
    color: var(--ink-light);
  }
  .card--mentor { top: 0; }
  .card--angel { top: 414px; }
  .card--designer { top: 828px; }
  .card__art { position: absolute; inset: 0; width: 653px; height: 372px; }
  .card__identity {
    position: absolute; left: 0; width: 220px; top: 124px;
    text-align: center;
  }
  .card__name { font-size: 21px; line-height: 26px; font-weight: 400; letter-spacing: 0.2px; }
  .card__title { font-size: 17.5px; line-height: 24px; margin-bottom: 14px; }
  .card__contact { font-size: 13px; line-height: 17px; letter-spacing: 0.4px; }
  .card__about {
    position: absolute; left: 262px; width: 372px;
    font-size: 16px; line-height: 22px;
  }
  .card--mentor .card__about { top: 120px; }
  .card--angel .card__about { top: 117px; font-size: 14.6px; line-height: 20.5px; width: 360px; }
  .card--designer .card__about { top: 104px; font-size: 14.6px; line-height: 21px; width: 370px; }
</style>
</head>
<body>
<main class="sheet">

  <svg width="0" height="0" style="position:absolute" aria-hidden="true">
    <defs>
      <clipPath id="card-shape"><rect x="0" y="0" width="653" height="372" rx="42"/></clipPath>
      <radialGradient id="paper-tone" cx="0.45" cy="0.4" r="0.8">
        <stop offset="0" stop-color="#f6efe1"/>
        <stop offset="0.6" stop-color="#ecdfc6"/>
        <stop offset="1" stop-color="#d9c197"/>
      </radialGradient>
      <g id="card-base">
        <g clip-path="url(#card-shape)">
          <rect width="653" height="372" fill="var(--orange)"/>
          <rect x="12" y="12" width="629" height="348" rx="34" fill="url(#paper-tone)" role="img" aria-label="Worn parchment texture"/>
          <rect x="0" y="90" width="653" height="190" fill="var(--orange)"/>
          <circle cx="92" cy="182" r="162" fill="var(--orange)"/>
          <circle cx="92" cy="182" r="152" fill="var(--brown)"/>
          <circle cx="92" cy="182" r="148" fill="var(--cream)"/>
          <circle cx="92" cy="182" r="141" fill="var(--brown)"/>
        </g>
      </g>
    </defs>
  </svg>

  <article class="card card--mentor">
    <svg class="card__art" viewBox="0 0 653 372" aria-hidden="true"><use href="#card-base"/></svg>
    <div class="card__identity">
      <h2 class="card__name">Tudor Vasilache</h2>
      <p class="card__title">Vocational Mentor</p>
      <p class="card__contact">info@tudorvasilache.example<br>www.tudorvasilache.example<br>+40745-TUDORV</p>
    </div>
    <p class="card__about">I help people to find their vocation and live happily from it. I use my 20 years of experience in business, management and psychology to help them identify the most efficient ways to make a living doing what they are passionate about.</p>
  </article>

  <article class="card card--angel">
    <svg class="card__art" viewBox="0 0 653 372" aria-hidden="true"><use href="#card-base"/></svg>
    <div class="card__identity">
      <h2 class="card__name">Tudor Vasilache</h2>
      <p class="card__title">Business Angel</p>
      <p class="card__contact">info@tudorvasilache.example<br>www.tudorvasilache.example<br>+40745-TUDORV</p>
    </div>
    <p class="card__about">I help founders to start a succesful business with minimum risks and costs. I use my 20 years of experience in sales, management and entrepreneurship to help them identify the most efficient ways, in terms of time and cost, to validate their business idea.</p>
  </article>

  <article class="card card--designer">
    <svg class="card__art" viewBox="0 0 653 372" aria-hidden="true"><use href="#card-base"/></svg>
    <div class="card__identity">
      <h2 class="card__name">Tudor Vasilache</h2>
      <p class="card__title">Learning Designer</p>
      <p class="card__contact">info@tudorvasilache.example<br>www.tudorvasilache.example<br>+40745-TUDORV</p>
    </div>
    <p class="card__about">I design unique learning programs that produce long-term cognitive and behavioural changes to people and organisations. I use my 20 years of experience in learning, teaching and change management to create minimalist experiences and processes that allows them to change efficiently in their pursued direction.</p>
  </article>

</main>
</body>
</html>
```